Flyer Handout when attending Dental Conventions, or dental office shows

take the sample file folder that is shown with 2 pictures. The outside and inside of the folder needs to be completed, along with the inserts. This folder pictures are from someone elses flyer/folder and i would like to have it layout like this. The KPW inserts is informational, but it is lacking originality, pictures, etc. Try to make our information and move it to 2017. When this is done, i would like to take this flyer and load it to the web or allow to send via email and make it interactive. The user can select the flyers and it will slide or flip to the flyer. this will make if kewl/fun

Target Market(s)

Dental Offices

Industry/Entity Type

Dental

Font styles to use
Serif
Sans Serif

Colors

Designer to choose colors to be used in the design.

Requirements
Must have
• a Semi new look and feel of our flyers, and a new envelope created

```html
<!DOCTYPE html>
<html lang="en">
<head>
<meta charset="utf-8">
<title>KPW Presentation Folder</title>
<link rel="stylesheet" href="https://fonts.googleapis.com/css2?family=Lato:wght@400;700;900&display=swap">
<style>
  :root {
    --sky: #3ea1d6;
    --sky-deep: #2e97cf;
    --brand-blue: #1d8bd0;
    --orange: #f7993a;
    --ink: #2a2a2a;
    --paper: #ffffff;
    --mist: #eef0f2;
    --shadow: rgba(0,0,0,0.28);
  }
  * { margin: 0; padding: 0; box-sizing: border-box; }
  html, body { width: 1200px; height: 1200px; overflow: hidden; background: var(--paper); }
  body { position: relative; font-family: "Lato", Arial, sans-serif; color: var(--ink); }
  .panel { position: absolute; box-shadow: 3px 3px 4px var(--shadow); }

  /* outside spread */
  .back-cover { left: 303px; top: 62px; width: 330px; height: 423px; background: var(--sky); }
  .back-cover .photo-tint { position: absolute; inset: 0;
    background: radial-gradient(ellipse at 55% 40%, #58b0de 0%, var(--sky) 60%, #3a9dd3 100%); }
  .contact { position: absolute; left: 0; right: 0; top: 187px; text-align: center; color: #fff; font-size: 7px; line-height: 1; }
  .contact .company { color: var(--orange); font-weight: 700; font-size: 8.5px; margin-bottom: 11px; }
  .contact p { margin-bottom: 5px; }
  .contact .gap { margin-top: 7px; }

  .front-cover { left: 634px; top: 67px; width: 331px; height: 417px; background: var(--paper); }
  .brand-mark { position: absolute; left: 0; right: 0; top: 16px; display: flex; align-items: center; justify-content: center; gap: 8px; }
  .brand-mark .name { font-weight: 900; font-size: 54px; color: var(--brand-blue); letter-spacing: 1px; line-height: 1; }
  .brand-mark .dot { width: 18px; height: 18px; border-radius: 50%; background: var(--orange); }
  .front-photo { position: absolute; left: 0; top: 98px; width: 331px; height: 319px;
    background: linear-gradient(135deg, #e9ecef 0%, #d9dde1 40%, #e6b8a0 65%, #5fb6cf 100%); }

  /* inside spread */
  .inside-left { left: 333px; top: 704px; width: 312px; height: 400px; background: var(--paper); }
  .inside-left .photo-fade { position: absolute; inset: 0;
    background: linear-gradient(180deg, #fafafa 0%, #f3f4f5 45%, #e4e6e8 100%); }
  .welcome { position: absolute; left: 0; right: 0; top: 24px; text-align: center; font-weight: 700; line-height: 1.15; }
  .welcome .lead { color: var(--brand-blue); font-size: 20px; }
  .welcome .company { color: var(--orange); font-size: 17.5px; }
  .intro { position: absolute; left: 51px; width: 221px; top: 103px; font-size: 6.2px; line-height: 7.7px; text-align: justify; color: var(--ink); }
  .intro p { margin-bottom: 7.5px; }
  .rule { position: absolute; left: 119px; top: 247px; width: 90px; height: 1px; background: var(--sky); }

  .inside-right { left: 645px; top: 704px; width: 315px; height: 402px; background: var(--sky-deep); }
  .ghost-name { position: absolute; font-weight: 900; line-height: 1; color: rgba(255,255,255,0.16); letter-spacing: 2px; }
  .inside-right .ghost-name { left: 0; right: 0; top: 80px; text-align: center; font-size: 96px; color: rgba(255,255,255,0.14); }

  .pockets { position: absolute; left: 0; top: 0; width: 1200px; height: 1200px; pointer-events: none; }
  .pocket { fill: var(--orange); }
  .pocket-ghost { font-family: "Lato", Arial, sans-serif; font-weight: 900; fill: rgba(255,255,255,0.2); }
</style>
</head>
<body>

  <section class="panel back-cover">
    <div class="photo-tint" role="img" aria-label="Blue-tinted photo of a smiling couple"></div>
    <div class="contact">
      <p class="company">Keystone Practice Works</p>
      <p>218 Alder Avenue</p>
      <p>Fairview, MN 55100</p>
      <p class="gap">Toll Free &nbsp;- 800-555-0142</p>
      <p class="gap">Telephone &nbsp;- 651-555-0178</p>
      <p class="gap">FAX &nbsp;- 651-555-0193</p>
    </div>
  </section>

  <section class="panel front-cover">
    <div class="brand-mark"><span class="name">KPW</span><span class="dot"></span></div>
    <div class="front-photo" role="img" aria-label="Photo of a patient in a dental chair being examined by a gloved dentist"></div>
  </section>

  <section class="panel inside-left">
    <div class="photo-fade" role="img" aria-label="Faded photo of a dentist at work"></div>
    <h1 class="welcome"><span class="lead">WELCOME TO</span><br><span class="company">Keystone Practice Works</span></h1>
    <div class="intro">
      <p>KPW is one of the largest electronic dental clearinghouses for dental claims and a leader in providing dental EDI solutions. We focus on bringing together Payers, Providers and Vendors to promote EDI transactions. Thousands of Dentists have chosen KPW as their electronic dental claims vendor of choice. Using our technology, KPW allows you to submit dental claims in seconds, the submission of Real Time Claim Statuses, Real Time Eligibility and getting Electronic Remittance Advice's (ERA's).</p>
      <p>KPW allows you to take your Electronic Remittance Advice (ERA) and post it directly into your Practice Management Software.</p>
      <p>Using Internet technology, KPW allows you to submit dental claims in minutes, access claim status in real time, and even submit all claims to all payers with a single click of the mouse. KPW also helps you connect directly to your payers, making it possible to cut weeks off your payment cycle.</p>
    </div>
    <div class="rule"></div>
  </section>

  <section class="panel inside-right">
    <div class="ghost-name">KPW</div>
  </section>

  <svg class="pockets" viewBox="0 0 1200 1200" aria-hidden="true">
    <g filter="drop-shadow(3px 3px 2px rgba(0,0,0,0.28))">
      <polygon class="pocket" points="303,490 311,484 633,484 621,624 309,624 303,617"/>
      <polygon class="pocket" points="634,484 958,484 965,495 965,545 957,557 644,557"/>
      <polygon class="pocket" points="333,1040 341,1035 636,1035 645,1104 339,1104 333,1097"/>
      <polygon class="pocket" points="658,971 943,971 960,982 960,1093 946,1106 645,1106"/>
    </g>
    <text class="pocket-ghost" x="458" y="528" font-size="72" text-anchor="middle" transform="rotate(180 458 554)">KPW</text>
    <text class="pocket-ghost" x="802" y="1062" font-size="78" text-anchor="middle">KPW</text>
  </svg>

</body>
</html>
```